Stationary Design needed for Physical Therapy and Wellness Center

Letterhead, Envelopes, Business Cards (x2) needed. We are a studio specializing in helping our clients improve mobility, fitness, and recover from injury. We use the Spirolane method and need to adhere to their trademark restrictions.

Target Market(s)

Potential Clients: active people...many from dance or athletic backgrounds.

Industry/Entity Type

Health And Wellness

Font styles to use
Sans Serif
Other font styles liked:
• Times New Roman for the word Spirolane.

Colors
00a990
33b8a4
86cfc6
0393ce
33a6d7
85cae6

Requirements
Must have
• Attention to Spirolane trademark guidelines (Times New Roman font, Bold type, use of registered trademark symbol). Examples of current stationary can be provided as an example.
• Concept of movement, flow.

```html
<!DOCTYPE html>
<html lang="en">
<head>
<meta charset="utf-8">
<title>Kinetra Business Cards</title>
<link href="https://fonts.googleapis.com/css2?family=Mulish:wght@400;600;700&family=Tinos:wght@700&display=swap" rel="stylesheet">
<style>
  :root {
    --teal: #00a990;
    --teal-soft: #33b8a4;
    --backdrop: #a9a9a9;
    --paper: #f7f7f5;
    --ink: #3a3a3a;
    --rule: #555555;
    --charcoal: #2f2f2f;
    --emboss: #1c1c1c;
  }
  * { margin: 0; padding: 0; box-sizing: border-box; }
  html, body { width: 1200px; height: 857px; overflow: hidden; }
  body {
    background: var(--backdrop);
    font-family: "Mulish", sans-serif;
    position: relative;
  }
  .card {
    position: absolute;
    top: 280px;
    width: 520px;
    height: 297px;
    border-bottom: 4px solid var(--teal);
    box-shadow: 0 10px 24px rgba(0,0,0,0.25);
  }
  .card--front { left: 60px; background: var(--paper); }
  .card--back { left: 620px; background: var(--charcoal); }

  .brand {
    position: absolute;
    display: flex;
    align-items: center;
    gap: 10px;
  }
  .brand__dot {
    width: 14px; height: 14px; border-radius: 50%;
    background: currentColor;
  }
  .brand__name {
    font-weight: 700;
    font-size: 40px;
    letter-spacing: -0.5px;
  }
  .card--front .brand { left: 40px; top: 124px; color: var(--teal); }
  .card--back .brand { left: 50%; top: 50%; transform: translate(-50%, -50%); color: var(--emboss); }
  .card--back .brand__name { font-size: 48px; }

  .divider {
    position: absolute;
    left: 232px; top: 62px;
    width: 1px; height: 174px;
    background: var(--rule);
  }
  .details {
    position: absolute;
    left: 256px; top: 58px;
    color: var(--ink);
  }
  .details__name {
    color: var(--teal);
    font-weight: 700;
    font-size: 17px;
    margin-bottom: 4px;
  }
  .details__role { font-size: 11.5px; line-height: 16px; white-space: nowrap; }
  .trademark {
    font-family: "Times New Roman", "Tinos", serif;
    font-weight: 700;
    font-size: 12.5px;
  }
  .contacts { list-style: none; margin-top: 16px; }
  .contacts li {
    display: flex; align-items: center; gap: 8px;
    font-size: 11.5px; line-height: 19px;
  }
  .contacts svg { width: 13px; height: 13px; flex: none; }
</style>
</head>
<body>
  <section class="card card--front">
    <div class="brand">
      <span class="brand__dot"></span>
      <span class="brand__name">kinetra</span>
    </div>
    <div class="divider"></div>
    <div class="details">
      <p class="details__name">Daniel Hollis, MSPT, ATC</p>
      <p class="details__role">Licensed Physical Therapist</p>
      <p class="details__role">Certified Athletic Trainer</p>
      <p class="details__role">Certified <span class="trademark">SPIROLANE®</span> Instructor</p>
      <p class="details__role">Figure Skating Coach</p>
      <ul class="contacts">
        <li>
          <svg viewBox="0 0 16 16"><circle cx="8" cy="8" r="8" fill="var(--teal)"/><path d="M5 4.5l1.6-.4 1 2-1 .8a5 5 0 0 0 2.5 2.5l.8-1 2 1-.4 1.6c-3.6.2-6.7-2.9-6.5-6.5z" fill="#fff"/></svg>
          <span>555-014-2290</span>
        </li>
        <li>
          <svg viewBox="0 0 16 16"><circle cx="8" cy="8" r="8" fill="var(--teal)"/><rect x="4" y="5" width="8" height="6" fill="#fff"/><path d="M4 5l4 3.2L12 5" fill="none" stroke="var(--teal)" stroke-width="1"/></svg>
          <span>daniel@kinetrapt.com</span>
        </li>
        <li>
          <svg viewBox="0 0 16 16"><circle cx="8" cy="8" r="8" fill="var(--teal)"/><circle cx="8" cy="8" r="4.2" fill="none" stroke="#fff" stroke-width="1"/><ellipse cx="8" cy="8" rx="1.8" ry="4.2" fill="none" stroke="#fff" stroke-width="1"/><path d="M3.8 8h8.4" stroke="#fff" stroke-width="1"/></svg>
          <span>www.kinetrapt.com</span>
        </li>
      </ul>
    </div>
  </section>

  <section class="card card--back">
    <div class="brand">
      <span class="brand__dot"></span>
      <span class="brand__name">kinetra</span>
    </div>
  </section>
</body>
</html>
```